Business Advisory Cards in canvas model

I need a business card to start as an individual advising in business since I am "Bachelor in Business Creation and business innovation" I would like the "Canvas Model" (basic tool to land a business) to represent a part of the logo because it is the simplest and useful model to start, I will advise on business innovation and business creation. Detail: it can be formal, dynamic, colorful, that draws attention, adapted to the millenians.

Target Market(s)

People who want to create their own company. People seeking advice on: negotiation, innovation in business, desing thingking, business creation, coaching in organizational operations, business plan and canvas model.

Contact Information for Business Card

Puede ser colorida pero formal para negociar, que se vea moderna adaptada a los millenians, que se enfoque en “el modelo canvas”.
Que ocupe toda la tarjeta de ambos lados todo el diseño.

Font styles to use
Sans Serif

Colors

Designer to choose colors to be used in the design.

Requirements
Must have
• Canvas model
Nice to have
• Make it a card that makes the person who receives it want to contact the owner of the card. Make it pleasing to the eye.
Should not have
• Negative images, colors that are lost or damage the eyesight.

```html
<!DOCTYPE html>
<html lang="es">
<head>
<meta charset="utf-8">
<title>Elías Navarro · Tarjeta de asesoría</title>
<link rel="stylesheet" href="https://fonts.googleapis.com/css2?family=Fira+Sans:wght@400;700;800&family=Open+Sans:wght@400;600&display=swap">
<style>
  :root {
    --page: #ffffff;
    --card-top: #1b1f27;
    --card-bottom: #0b0c0f;
    --ink: #050505;
    --mark: #3a3d43;
    --red: #e8262b;
    --orange: #f7921e;
    --blue: #3d7cc9;
    --green: #3aaa48;
    --spectrum: linear-gradient(90deg, #e81d4f 0%, #c2245a 9%, #2a3f9e 16%, #1f5fb5 25%, #4cc2ea 33%, #d6eef5 40%, #4ab56a 48%, #2f9e46 56%, #9ccc47 64%, #c9dd4d 72%, #f2ea22 82%, #f7c51e 92%, #f7941d 100%);
  }
  * { box-sizing: border-box; margin: 0; padding: 0; }
  html, body { width: 1200px; height: 1200px; overflow: hidden; background: var(--page); }
  .canvas { position: relative; width: 1200px; height: 1200px; }

  .card {
    position: absolute;
    width: 721px;
    height: 410px;
    background: linear-gradient(180deg, var(--card-top) 0%, var(--card-top) 45%, var(--card-bottom) 100%);
    overflow: hidden;
  }
  .card--front { left: 200px; top: 146px; }
  .card--back { left: 202px; top: 616px; }

  .spectrum-band {
    position: absolute; left: 0; top: 0; width: 100%;
    background: var(--spectrum);
  }
  .card--front .spectrum-band { height: 39px; }
  .card--back .spectrum-band { height: 194px; }

  .brand-mark {
    position: absolute; left: 0; right: 0; top: 190px;
    display: flex; align-items: center; justify-content: center; gap: 16px;
  }
  .brand-mark__square { width: 26px; height: 26px; background: var(--mark); }
  .brand-mark__name {
    font-family: "Fira Sans", sans-serif; font-weight: 700;
    font-size: 40px; color: var(--mark); letter-spacing: 1px;
  }

  .identity { position: absolute; left: 167px; top: 78px; color: var(--ink); }
  .identity__name {
    font-family: "Fira Sans", sans-serif; font-weight: 800;
    font-size: 47px; letter-spacing: 5px; line-height: 1;
  }
  .identity__name .surname { font-weight: 700; }
  .identity__role {
    margin-top: 9px;
    font-family: "Fira Sans", sans-serif; font-size: 24px; letter-spacing: 1px; line-height: 1;
  }
  .identity__role strong { font-weight: 700; margin-left: 10px; }

  .contact { position: absolute; display: flex; align-items: center; gap: 14px; }
  .contact__icon {
    width: 39px; height: 39px; flex: none;
    display: flex; align-items: center; justify-content: center;
  }
  .contact__icon svg { width: 22px; height: 22px; }
  .contact__text {
    font-family: "Open Sans", sans-serif; font-weight: 600;
    font-size: 11px; line-height: 15px; text-transform: uppercase;
  }
  .contact--email { left: 76px; top: 242px; }
  .contact--phone { left: 76px; top: 306px; }
  .contact--address { left: 459px; top: 242px; }
  .contact--web { left: 459px; top: 306px; }
  .contact--email .contact__icon { background: var(--red); }
  .contact--email .contact__text { color: var(--red); }
  .contact--phone .contact__icon { background: var(--orange); }
  .contact--phone .contact__text { color: var(--orange); }
  .contact--address .contact__icon { background: var(--blue); }
  .contact--address .contact__text { color: var(--blue); font-size: 10px; }
  .contact--web .contact__icon { background: var(--green); }
  .contact--web .contact__text { color: var(--green); }

  .color-rule { position: absolute; left: 0; bottom: 0; width: 100%; height: 3px; display: flex; }
  .color-rule span:nth-child(1) { width: 29%; background: var(--red); }
  .color-rule span:nth-child(2) { width: 30.4%; background: var(--orange); }
  .color-rule span:nth-child(3) { width: 31.2%; background: var(--blue); }
  .color-rule span:nth-child(4) { flex: 1; background: var(--green); }
</style>
</head>
<body>
<main class="canvas">

  <section class="card card--front" aria-label="Anverso">
    <div class="spectrum-band" role="img" aria-label="Banda de mosaico poligonal multicolor"></div>
    <div class="brand-mark">
      <span class="brand-mark__square"></span>
      <span class="brand-mark__name">LienzoNegocio</span>
    </div>
  </section>

  <section class="card card--back" aria-label="Reverso">
    <div class="spectrum-band" role="img" aria-label="Fondo de mosaico poligonal multicolor"></div>
    <div class="identity">
      <h1 class="identity__name">ELÍAS <span class="surname">NAVARRO</span></h1>
      <p class="identity__role">Consultor <strong>LienzoNegocio</strong></p>
    </div>

    <div class="contact contact--email">
      <div class="contact__icon">
        <svg viewBox="0 0 24 24"><rect x="2" y="5" width="20" height="14" fill="#111"/><path d="M3 6l9 7 9-7M3 18l7-6M21 18l-7-6" stroke="#e8262b" stroke-width="1.4" fill="none"/></svg>
      </div>
      <p class="contact__text">hola@lienzonegocio.com</p>
    </div>

    <div class="contact contact--phone">
      <div class="contact__icon">
        <svg viewBox="0 0 24 24"><path d="M6.6 3.5l3 3.2-1.8 2.2c1.2 2.6 3.2 4.6 5.8 5.8l2.2-1.8 3.2 3-1.9 3.1C10.6 19 5 13.4 3.5 5.4z" fill="#111"/></svg>
      </div>
      <p class="contact__text">+1 555 0142 3861<br>+1 555 0197 2450</p>
    </div>

    <div class="contact contact--address">
      <div class="contact__icon">
        <svg viewBox="0 0 24 24"><path d="M12 3L2 12h3v8h5v-5h4v5h5v-8h3z" fill="#111"/></svg>
      </div>
      <p class="contact__text">Your city address<br>Street location, NY city, USA</p>
    </div>

    <div class="contact contact--web">
      <div class="contact__icon">
        <svg viewBox="0 0 24 24"><circle cx="12" cy="12" r="9" fill="none" stroke="#111" stroke-width="2"/><path d="M8 7c2 0 3 1 2.5 3S8 11 8.5 13s2 2 1.5 4M15 6c-1 2 1 3 2.5 3.5M14 14c1.5-1 3 0 3.5 1.5" stroke="#111" stroke-width="2" fill="none"/></svg>
      </div>
      <p class="contact__text">www.lienzonegocio.com</p>
    </div>

    <div class="color-rule"><span></span><span></span><span></span><span></span></div>
  </section>

</main>
</body>
</html>
```